Corporate Web Redesign Project - coded

We would like redesign/refresh of our current site that would allow us to increase the depth of content and create a high quality impression for visitors.

Current site - http://corvanisystems.com/

A previous web redesign project has improved our site but it has not really reached the level we require.

Our customers are global, blue chip, organisations and a professional, corporate style of site is required.

Please note we would prefer a coded website to a just a design. We are happy to provide a zip of our current site if required.
Updates

                                   

Target Market(s)

Global oil and gas producers, KR, Tamberline, Orvadex etc.

Industry/Entity Type

It Professional

Requirements
Must have
• Design should support the level of content we currently have in the existing sitemap - although it should be expandable a site design for a large / complex site would not be appropriate

All current content / pages to be reflected in design

Must be visually appealing

Intuitive and clear navigation that is expandable

Display a high level of professionalism

Use a consistent palette of colours that complements our logo

Clean and organized layout

A way to capture visitor’s information or Call to action (i.e. contact link or form) on every page

Prominent Contact Information
Should not have
• Flash

```html
<!DOCTYPE html>
<html lang="en">
<head>
<meta charset="utf-8">
<title>Corvani Systems – The Business of Drilling Wells</title>
<link href="https://fonts.googleapis.com/css2?family=Arimo:wght@400;700&family=Lato:wght@300;400&family=Roboto+Condensed:wght@400&display=swap" rel="stylesheet">
<style>
:root{
  --teal:#4a7d87;
  --teal-text:#3e7a86;
  --page:#ececec;
  --band:#f4f4f4;
  --white:#ffffff;
  --ink:#333333;
  --muted:#7a7a7a;
  --rule:#bdbdbd;
  --accent:#2bc3e8;
  --orange:#ff8200;
  --icon:#4a4a4a;
}
*{margin:0;padding:0;box-sizing:border-box}
html,body{width:947px;height:1200px;overflow:hidden;background:var(--page)}
body{font-family:Arimo,Arial,sans-serif;color:var(--ink)}
.site{position:relative;width:947px;height:1200px;overflow:hidden}
.sheet{position:absolute;left:10px;top:0;width:926px;height:1200px;background:var(--white)}
.abs{position:absolute}

.header{left:10px;top:0;width:926px;height:106px;background:var(--band)}
.brand{left:94px;top:38px;display:flex;align-items:center;gap:8px;font-weight:700;font-size:18px;color:var(--teal-text);letter-spacing:.5px}
.brand-dot{width:16px;height:16px;border-radius:50%;background:var(--teal)}
.nav{left:474px;top:32px;display:flex;height:43px;background:var(--white)}
.nav a{display:flex;align-items:center;justify-content:center;font-size:11.5px;color:#999;text-decoration:none;border-right:1px solid #eee}
.nav a.active{background:var(--teal);color:#fff;font-weight:700}

.hero-title{left:110px;top:143px;font-family:Lato,sans-serif;font-weight:400;color:#222;font-size:29px;line-height:1}
.hero-title span{display:block;color:var(--teal-text);font-size:39px;font-weight:300;margin-top:4px}
.hero-visual{left:540px;top:120px;width:280px;height:250px;background:radial-gradient(ellipse at 55% 55%,#9a9a9a 0%,#cfcfcf 35%,#f4f4f4 62%,#fff 75%)}
.hero-cta{left:111px;top:250px;width:422px;height:49px;background:var(--teal);color:#fff;font-family:Lato,sans-serif;font-size:19px;white-space:nowrap;display:flex;align-items:center;padding-left:10px;z-index:2}
.hero-rule{left:10px;top:369px;width:926px;height:3px;background:var(--teal)}
.tab-strip{left:10px;top:372px;width:926px;height:42px;background:var(--band)}
.tab{top:373px;width:174px;height:41px;background:var(--white);box-shadow:0 0 3px rgba(0,0,0,.12);font-family:"Roboto Condensed",sans-serif;font-size:14px;color:var(--teal-text);display:flex;align-items:center;justify-content:center}

.feature{top:425px;width:174px;text-align:center}
.feature svg{display:block;margin:0 auto;height:56px}
.feature .rule{margin:20px auto 0;width:152px;height:1px;background:#888;position:relative}
.feature .rule::after{content:"";position:absolute;left:52px;top:-1px;width:48px;height:2px;background:var(--accent)}
.feature p{margin:20px auto 0;width:150px;height:44px;font-size:9.2px;line-height:14.5px;color:var(--muted)}
.more{display:inline-block;margin-top:22px;padding:7px 13px;border-radius:14px;background:#f5f5f5;box-shadow:0 1px 2px rgba(0,0,0,.2);font-family:Lato,sans-serif;font-size:9.5px;color:#888}

.section-head{font-family:"Roboto Condensed",sans-serif;font-weight:400;font-size:26px;color:var(--teal-text);display:flex;align-items:center;gap:8px}
.section-head::after{content:"";flex:1;height:1px;background:var(--rule)}
.about-head{left:96px;top:652px;width:370px}
.news-head{left:502px;top:652px;width:350px}
.body-copy{font-size:10px;line-height:16px;color:var(--muted);text-align:justify}
.about-copy{left:99px;top:695px;width:367px}
.about-copy p+p{margin-top:15px}
.news{left:502px;top:694px;width:350px}
.news h3{font-weight:400;font-size:13.5px;color:var(--teal-text);letter-spacing:.3px;margin-bottom:8px}
.news p+h3{margin-top:16px}

.partners{left:94px;top:864px;width:760px;height:115px;border:1px solid #bbb;display:flex;align-items:center;justify-content:space-around;background:var(--white)}
.partner{display:flex;align-items:center;gap:5px;font-size:12px;color:#777}
.partner i{display:block;width:10px;height:10px;background:#9a9a9a}

.footer{left:10px;top:1021px;width:926px;height:179px;background:var(--band);border-top:1px solid #c8c8c8}
.footer-rule{left:10px;top:1151px;width:926px;height:1px;background:#cfcfcf}
.address{font-size:10.2px;line-height:16px;color:#444}
.addr-eu{left:100px;top:1049px;width:150px;text-align:right}
.addr-us{left:669px;top:1049px;width:200px}
.map-eu{left:265px;top:1033px;width:112px;height:91px;background:var(--orange)}
.map-us{left:562px;top:1028px;width:82px;height:96px;background:var(--orange);border-radius:30% 40% 45% 20%}
.connect{left:380px;top:1064px;width:180px;text-align:center;font-family:"Roboto Condensed",sans-serif;font-size:19px;color:var(--teal-text)}
.copyright{left:10px;top:1171px;width:926px;text-align:center;font-size:10.2px;color:#444}
</style>
</head>
<body>
<div class="site">
  <div class="sheet"></div>

  <header class="header abs"></header>
  <div class="brand abs"><span class="brand-dot"></span>CORVANI SYSTEMS</div>
  <nav class="nav abs">
    <a class="active" href="#" style="width:75px">Home</a>
    <a href="#" style="width:64px">News</a>
    <a href="#" style="width:78px">About Us</a>
    <a href="#" style="width:78px">Solutions</a>
    <a href="#" style="width:83px;border-right:0">Contact Us</a>
  </nav>

  <h1 class="hero-title abs">THE BUSINESS OF<span>DRILLING WELLS</span></h1>
  <div class="hero-visual abs" role="img" aria-label="Offshore drilling platform rendering"></div>
  <div class="hero-cta abs">Unterstand &amp; communicate project cost &amp; risk</div>
  <div class="hero-rule abs"></div>
  <div class="tab-strip abs"></div>
  <div class="tab abs" style="left:98px">Time &amp; Cost Estimation</div>
  <div class="tab abs" style="left:290px">Materials &amp; Cost Control</div>
  <div class="tab abs" style="left:482px">Lessons Learned</div>
  <div class="tab abs" style="left:675px">Services &amp; Consulting</div>

  <div class="feature abs" style="left:98px">
    <svg viewBox="0 0 40 52" width="40"><g fill="var(--icon)"><rect x="1" y="20" width="4" height="24"/><rect x="8" y="12" width="4" height="32"/><rect x="15" y="2" width="4" height="42"/><rect x="22" y="10" width="4" height="34"/><rect x="29" y="18" width="4" height="26"/><rect x="36" y="26" width="3" height="18"/><rect x="1" y="46" width="38" height="4"/></g></svg>
    <div class="rule"></div>
    <p>RPQ delivers a standardized, systematic approach to understanding project risk.</p>
    <span class="more">READ MORE</span>
  </div>
  <div class="feature abs" style="left:290px">
    <svg viewBox="0 0 40 52" width="40"><rect x="2" y="1" width="36" height="50" rx="5" fill="none" stroke="var(--icon)" stroke-width="3"/><rect x="8" y="7" width="24" height="6" fill="var(--icon)"/><g fill="none" stroke="var(--icon)" stroke-width="2.5"><rect x="7" y="18" width="12" height="12" rx="2"/><rect x="21" y="18" width="12" height="12" rx="2"/><rect x="7" y="33" width="12" height="12" rx="2"/><rect x="21" y="33" width="12" height="12" rx="2"/></g><g stroke="var(--icon)" stroke-width="2"><path d="M10 24h6M13 21v6M24 24h6M10 36l6 6M16 36l-6 6M24 37h6M24 41h6"/></g></svg>
    <div class="rule"></div>
    <p>CLV has been helping companies optimize materials and cost tracking processes</p>
    <span class="more">READ MORE</span>
  </div>
  <div class="feature abs" style="left:482px">
    <svg viewBox="0 0 56 52" width="56"><path d="M14 4h38l-14 40H4z" fill="var(--icon)"/><path d="M4 44c0 5 3 6 6 6h34l2-5H10c-2 0-2-2 0-2" fill="none" stroke="var(--icon)" stroke-width="3"/><path d="M18 12h26M16 18h26" stroke="#fff" stroke-width="2"/></svg>
    <div class="rule"></div>
    <p>KNV is an advanced lessons learned &amp; knowledge system for use in the energy industry.</p>
    <span class="more">READ MORE</span>
  </div>
  <div class="feature abs" style="left:675px">
    <svg viewBox="0 0 46 52" width="46"><circle cx="23" cy="14" r="11" fill="var(--icon)"/><path d="M2 50c0-14 8-20 21-20s21 6 21 20z" fill="var(--icon)"/><path d="M20 31l3 12 3-12z" fill="#fff"/></svg>
    <div class="rule"></div>
    <p>Successful software implementations rely on people and processes to deliver results.</p>
    <span class="more">READ MORE</span>
  </div>

  <h2 class="section-head about-head abs">ABOUT US</h2>
  <div class="body-copy about-copy abs">
    <p>From early phase evaluation through planning, execution and post analysis of wells, we deliver the tools, processes and people required to facilitate major performance improvement and cost savings.</p>
    <p>Our solutions are used in more than 30 countries to support operations ranging from a single well to global deployments with Major Operators.</p>
  </div>

  <h2 class="section-head news-head abs">LATEST NEWS</h2>
  <div class="news abs">
    <h3>RPQ Selected by Marrowind</h3>
    <p class="body-copy">Marrowind Energy Ltd has selected RPQ as the solution to provide probabilistic time and cost estimates for its drilling operations.</p>
    <h3>CLV Implementation at Lysander Energy</h3>
    <p class="body-copy">Lysander Energy selects CLV to support its materials, logistics &amp; cost management processes.</p>
  </div>

  <div class="partners abs">
    <span class="partner"><i></i>KR</span>
    <span class="partner">Talvera</span>
    <span class="partner">Marrowind</span>
    <span class="partner">Quorin</span>
    <span class="partner">Brantley</span>
    <span class="partner">Lysander</span>
    <span class="partner">Orvadex</span>
  </div>

  <footer class="footer abs"></footer>
  <div class="address addr-eu abs">27 Kestrel Row<br>Aberdeen<br>AB10 4QT<br>Phone:+44(0)1224 000418<br>Email: eu@corvanisystems.com</div>
  <div class="map-eu abs" role="img" aria-label="Map of Europe"></div>
  <div class="connect abs">CONNECT WITH US</div>
  <div class="map-us abs" role="img" aria-label="Map of North America"></div>
  <div class="address addr-us abs">1800 Meridian Park Blvd<br>Suite 200<br>Houston, TX 77042<br>Phone:(713) 555 0142<br>Email: us@corvanisystems.com</div>
  <div class="footer-rule abs"></div>
  <div class="copyright abs">Copyright ©2013 Corvani Systems. Designed by Northpass Designs</div>
</div>
</body>
</html>
```